Need a professional card design. Tallowmere building company specialise in residential and commercial builds. New homes, additions & renovations.
Wanting a card with creativity and professionalism.
Want card that utilises logo.

Back and front.

I have just created a logo, and want to use it on the business card.
Attached a copy of the logo.
Attached is also a current business card which I wish to redesign

please utilise both sides

Residential

• Reg# 58306

```html
<!DOCTYPE html>
<html lang="en">
<head>
<meta charset="utf-8">
<title>Tallowmere Building Co – Business Card</title>
<link rel="stylesheet" href="https://fonts.googleapis.com/css2?family=Roboto+Slab:wght@700&family=Ubuntu:wght@400;500&display=swap">
<style>
  :root {
    --stage: #2b2b2b;
    --card-dark: #231e1b;
    --card-light: #ffffff;
    --ink: #1a1a1a;
    --amber: #e09a22;
    --silver: #e6e6e6;
  }
  * { margin: 0; padding: 0; box-sizing: border-box; }
  html, body { width: 1200px; height: 900px; overflow: hidden; }
  body {
    background: var(--stage);
    font-family: "Ubuntu", sans-serif;
    position: relative;
  }
  .card {
    position: absolute;
    left: 300px;
    width: 600px;
    height: 343px;
    border-radius: 2px;
    box-shadow: 0 12px 30px rgba(0,0,0,.5);
  }
  .card--back { top: 70px; background: var(--card-dark); }
  .card--front { top: 487px; background: var(--card-light); color: var(--ink); }

  /* back */
  .back-brand {
    position: absolute; left: 0; right: 0; top: 120px;
    text-align: center;
    font-weight: 500; font-size: 40px; letter-spacing: 1px;
    color: var(--silver);
  }
  .back-reg {
    position: absolute; left: 0; right: 0; top: 190px;
    text-align: center;
    font-family: "Roboto Slab", serif; font-weight: 700;
    font-size: 24px; color: var(--silver); letter-spacing: 1px;
  }
  .back-reg .reg-number { color: var(--amber); }

  /* front */
  .services {
    position: absolute; left: 330px; top: 40px;
    font-size: 12.5px; font-weight: 500; line-height: 1.35;
  }
  .chevron { position: absolute; left: 270px; top: 36px; }
  .person { position: absolute; left: 40px; top: 92px; }
  .person-name {
    font-family: "Roboto Slab", serif; font-weight: 700;
    font-size: 24px; letter-spacing: .5px;
  }
  .person-role {
    font-family: "Roboto Slab", serif; font-weight: 700;
    font-size: 21px; color: var(--amber);
  }
  .address {
    position: absolute; left: 40px; top: 182px;
    font-size: 13.5px; font-weight: 500; line-height: 1.35;
  }
  .contacts {
    position: absolute; left: 40px; top: 252px;
    font-size: 12px; line-height: 1.4; list-style: none;
  }
  .contacts .label { color: var(--amber); font-weight: 500; }
  .front-brand {
    position: absolute; right: 40px; top: 225px;
    font-weight: 500; font-size: 22px; color: var(--amber);
  }
</style>
</head>
<body>
  <section class="card card--back" aria-label="Card back">
    <div class="back-brand">Tallowmere Building Co</div>
    <div class="back-reg">REG NO. <span class="reg-number">58306</span></div>
  </section>

  <section class="card card--front" aria-label="Card front">
    <svg class="chevron" width="34" height="52" viewBox="0 0 34 52" aria-hidden="true">
      <polyline points="4,4 30,26 4,48" fill="none" stroke="var(--amber)" stroke-width="3"/>
    </svg>
    <p class="services">New Homes - Additions &amp; Renovations<br>Domestic &amp; Commercial Builders</p>

    <div class="person">
      <p class="person-name">MARA DELACROIX</p>
      <p class="person-role">Director</p>
    </div>

    <p class="address">27 Harbury Lane, Kelmsworth<br>WA 6031</p>

    <ul class="contacts">
      <li><span class="label">TEL:</span> 08 9417 2560</li>
      <li><span class="label">FAX:</span> 08 9417 2560</li>
      <li><span class="label">MOB:</span> 0422 615 394</li>
      <li><span class="label">EMAIL:</span> tallowmerebuildingco@mail.com</li>
    </ul>

    <div class="front-brand">Tallowmere Building Co</div>
  </section>
</body>
</html>
```